Update the A4 Specials Page for Restaurant/Cafe

Provide a MINIMALIST attractive Specials page we can print weekly for our food and drink specials to give to our guests. Final design is to be provided in WORD Document so it can be easily edited by Manager. Should be black text and MINIMALIST to minimise ink usage as we print hundreds a week. We have UPLOADED the existing page as a template for you to update. Maybe logo can stay, see what you think. Or delete it and do something else. Keep it simple. Choose a good FONT. Could be a little playful with a cocktail ICON or something. Our existing menus can be seen at www.tallpinebistro.com.au and they are using font Alegreya. Please note we are unable to provide any feedback to designers, however we really do appreciate your time if you are submitting a design. Thank you for your participation.

```html
<!DOCTYPE html>
<html lang="en">
<head>
<meta charset="utf-8">
<title>Tall Pine Bistro – Weekly Specials</title>
<link rel="stylesheet" href="https://fonts.googleapis.com/css2?family=Alegreya:wght@400;700;800&family=Josefin+Sans:wght@600&display=swap">
<style>
  :root {
    --ink: #000000;
    --paper: #ffffff;
    --backdrop: #ffffff;
    --muted: #1a1a1a;
  }
  html, body {
    margin: 0;
    padding: 0;
    width: 1200px;
    height: 1200px;
    overflow: hidden;
    background: var(--backdrop);
  }
  .canvas {
    position: relative;
    width: 1200px;
    height: 1200px;
  }
  .page {
    position: absolute;
    left: 192px;
    top: 19px;
    width: 1046px;
    height: 1490px;
    background: var(--paper);
    transform: scale(0.78);
    transform-origin: 0 0;
    font-family: "Alegreya", Georgia, serif;
    color: var(--ink);
  }
  .page-frame {
    position: absolute;
    left: 35px;
    top: 39px;
    width: 970px;
    height: 1407px;
    border: 2px dashed var(--ink);
  }
  .brand {
    position: absolute;
    left: 162px;
    top: 105px;
    width: 715px;
    height: 247px;
    margin: 0;
    text-align: center;
    font-family: "Alegreya", Georgia, serif;
    font-weight: 800;
    text-transform: uppercase;
    color: var(--ink);
    line-height: 1;
  }
  .brand-line {
    display: block;
  }
  .brand-line--top {
    font-size: 108px;
    letter-spacing: 0.02em;
    margin-top: 6px;
  }
  .brand-line--bottom {
    font-size: 120px;
    letter-spacing: 0.06em;
    margin-top: 10px;
  }
  .section-band {
    position: absolute;
    left: 57px;
    width: 931px;
    background: var(--ink);
    color: var(--paper);
    display: flex;
    align-items: center;
    justify-content: center;
    margin: 0;
    font-family: "Josefin Sans", Arial, sans-serif;
    font-weight: 600;
    font-size: 46px;
    letter-spacing: 0.42em;
    text-transform: uppercase;
  }
  .section-band .label {
    padding-top: 8px;
  }
  .band--weekly { top: 388px; height: 68px; }
  .band--weekly .label { margin-left: 0.42em; }
  .band--cocktail { top: 787px; height: 67px; }
  .band--cocktail .label { margin-left: 76px; }
  .band--beer { top: 1076px; height: 66px; }
  .band--beer .label { margin-right: 60px; }
  .band-icon {
    position: absolute;
    top: 50%;
    transform: translateY(-50%);
  }
  .band-icon--cocktail { left: 12px; }
  .band-icon--beer { right: 4px; }
  .item-title {
    position: absolute;
    left: 120px;
    width: 812px;
    height: 40px;
    display: flex;
    align-items: baseline;
    margin: 0;
    font-size: 31px;
    font-weight: 800;
    text-transform: uppercase;
  }
  .item-title .leader {
    flex: 1;
    border-bottom: 3px dotted var(--ink);
    margin: 0 8px;
    transform: translateY(-6px);
  }
  .item-title .price {
    font-size: 27px;
  }
  .item-detail {
    position: absolute;
    left: 120px;
    margin: 0;
    font-size: 20px;
    line-height: 34px;
    color: var(--muted);
  }
  .item-detail--strong {
    font-weight: 700;
    line-height: 44px;
    color: var(--ink);
  }
  .offer-note {
    position: absolute;
    left: 193px;
    top: 1378px;
    width: 650px;
    border-top: 2px dashed var(--ink);
    margin: 0;
    padding-top: 2px;
    text-align: center;
    font-size: 18px;
    color: var(--muted);
  }
</style>
</head>
<body>
<div class="canvas">
  <article class="page">
    <div class="page-frame"></div>

    <h1 class="brand">
      <span class="brand-line brand-line--top">Tall Pine</span>
      <span class="brand-line brand-line--bottom">Bistro</span>
    </h1>

    <h2 class="section-band band--weekly"><span class="label">Weekly Specials</span></h2>

    <h3 class="item-title" style="top:480px"><span>Chicken Filo</span><span class="leader"></span><span class="price">$ 24</span></h3>
    <p class="item-detail" style="top:539px">Creamy Chicken with Pinenuts, wrapped in Filo Pastry.<br>Served with Side Salad &amp; Zulu Sauce</p>

    <h3 class="item-title" style="top:628px"><span>Minestrone Soup</span><span class="leader"></span><span class="price">$ 8</span></h3>
    <p class="item-detail" style="top:687px">Served with Garlic Bread</p>

    <h2 class="section-band band--cocktail">
      <svg class="band-icon band-icon--cocktail" width="44" height="62" viewBox="0 0 44 62" fill="none" stroke="#ffffff" stroke-width="2" stroke-linecap="round" stroke-linejoin="round" aria-hidden="true">
        <path d="M4 14 H36 L20 34 Z"/>
        <line x1="20" y1="34" x2="20" y2="54"/>
        <ellipse cx="20" cy="56" rx="10" ry="3"/>
        <line x1="24" y1="22" x2="38" y2="6"/>
        <circle cx="39" cy="5" r="3"/>
      </svg>
      <span class="label">Cocktail Specials</span>
    </h2>

    <h3 class="item-title" style="top:879px"><span>Passionista</span><span class="leader"></span><span class="price">$17</span></h3>
    <p class="item-detail item-detail--strong" style="top:931px">Vodka, Passionfruit Pulp, Mango Puree<br>Top up with Ginger &amp; Lemon Kombucha</p>

    <h2 class="section-band band--beer">
      <span class="label">Craft Beer Special</span>
      <svg class="band-icon band-icon--beer" width="46" height="56" viewBox="0 0 46 56" fill="none" stroke="#ffffff" stroke-width="2.4" stroke-linecap="round" stroke-linejoin="round" aria-hidden="true">
        <path d="M4 12 C4 4 12 2 16 6 C20 1 28 2 30 8 C34 8 34 14 32 14"/>
        <rect x="4" y="12" width="28" height="40" rx="3"/>
        <path d="M32 20 H40 V42 H32"/>
        <line x1="12" y1="20" x2="12" y2="44"/>
        <line x1="20" y1="20" x2="20" y2="44"/>
      </svg>
    </h2>

    <h3 class="item-title" style="top:1166px"><span>Crooked Gecko</span><span class="leader"></span><span class="price">$ 10</span></h3>
    <p class="item-detail" style="top:1225px">FRUIT BURST<br>Tropical Pale Ale<br>4.8% Alc.</p>

    <p class="offer-note">SPECIAL OFFERS ARE VALID FROM 10 December 2023 – 16 December 2023</p>
  </article>
</div>
</body>
</html>
```